The Truths About Child Neglect

The goal of this info-graphic is to visually command the attention of our intended audience (teen/adult parents, teachers, youth program coordinators, etc.). Because this project has to do with children, the design should have pops of color; it should be an info-graphic that schools and non profit youth organizations would gladly welcome as an addition to their website. It is important though that the aesthetic, while stimulating the viewer, doesn't overpower the information. The final design should ultimately highlight the innocence of childhood.

Note: the information that has been uploaded is currently formatted in a mock-up info-graphic. Please do not follow that aesthetic; the above description is the route that we would like to take things.

Target Market(s)

Parents
Teachers
Youth Organizations
Parent Bloggers

Industry/Entity Type

Childcare

Font styles to use
Serif
Decorative

Colors

Designer to choose colors to be used in the design.

Requirements
Must have
• Visually captivating imagery
• The info-graphic should grab the viewers attention.
• Sources must be sited at the bottom in small print.
• Looks professional
Nice to have
• A story telling flow of imagery within the info-graphic, which makes it easier for viewers to follow the poignant details.
Should not have
• Boring imagery.
• Heavy text/too much wording.
• Lack of sited sources.

```html
<!DOCTYPE html>
<html lang="en">
<head>
<meta charset="utf-8">
<title>The Truths About Child Neglect</title>
<link href="https://fonts.googleapis.com/css2?family=Bebas+Neue&family=Oswald:wght@400;500&display=swap" rel="stylesheet">
<style>
:root{
  --navy:#15172e;
  --forest:#0e2622;
  --sky:#3cb6e8;
  --lime:#b9d53d;
  --sun:#f5e63a;
  --white:#ffffff;
  --alert:#f0492a;
  --money:#1f9a45;
  --paper:#fbf0c4;
}
*{margin:0;padding:0;box-sizing:border-box}
html,body{width:1200px;height:1200px;overflow:hidden;background:var(--white)}
.poster{position:relative;width:1200px;height:1200px;background:var(--white)}
.col{position:absolute;top:8px;height:1178px;overflow:hidden}
.col-charges{left:0;width:400px;background:var(--navy)}
.col-consequences{left:400px;width:400px;background:var(--forest)}
.col-avoid{left:800px;width:393px;background:var(--navy)}
.abs{position:absolute}
.txt{font-family:"Bebas Neue","Oswald",sans-serif;text-transform:uppercase;letter-spacing:.2px;line-height:30px;font-size:24px;white-space:nowrap}
.sky{color:var(--sky)}
.lime{color:var(--lime)}
.sun{color:var(--sun)}
.big-num{font-family:"Bebas Neue",sans-serif;color:var(--white);line-height:1;white-space:nowrap}
.head{font-family:"Bebas Neue",sans-serif;color:var(--white);line-height:1;font-weight:400;white-space:nowrap}
.art{position:absolute;border-radius:14px}
.penalties{list-style:none}
.penalties li{font-size:27px;line-height:35px}
.money{font-family:"Oswald",sans-serif;font-weight:500;color:var(--money);font-size:76px;letter-spacing:6px;line-height:1}
.note{font-family:"Bebas Neue",sans-serif;color:var(--white);font-size:23px;line-height:30px;white-space:nowrap}
.note .org{color:var(--alert)}
.sources-label{font-family:"Bebas Neue",sans-serif;color:var(--sun);font-size:23px;line-height:1}
.source-list{list-style:none;font-family:Arial,sans-serif;font-size:10px;line-height:13px;color:var(--white)}
.source-list li{text-decoration:underline;margin-bottom:4px;word-break:break-all}
</style>
</head>
<body>
<main class="poster">

  <section class="col col-charges">
    <div class="big-num abs" style="left:24px;top:22px;font-size:118px">8</div>
    <div class="head abs" style="left:72px;top:30px;font-size:33px">Ways you can be charged with</div>
    <h1 class="head abs" style="left:70px;top:54px;font-size:66px">Child Neglect</h1>

    <p class="txt sky abs" style="left:28px;top:134px">1. Leaving your child to play outside by<br>themselves, whether they are on your<br>property or not</p>
    <p class="txt lime abs" style="left:28px;top:236px">2. Leaving your<br>child in the car<br>unsupervised,<br>despite the length<br>of the time they<br>are left alone.</p>
    <div class="art" role="img" aria-label="Illustration of a child alone in a grey car" style="left:194px;top:250px;width:186px;height:162px;background:linear-gradient(160deg,#8d8f96,#5f6169)"></div>

    <p class="txt sky abs" style="left:28px;top:430px">3. Leaving your child home alone<br>without arranging for reasonable care<br>or supervision.</p>
    <div class="art" role="img" aria-label="Illustration of a crying child calling for mom" style="left:30px;top:528px;width:330px;height:108px;background:linear-gradient(90deg,#2a2c4a,#e4573a 50%,#2a2c4a)"></div>

    <p class="txt lime abs" style="left:28px;top:644px">4. Becoming emotionally or physically<br>combative with the other parent while<br>your child is present.</p>
    <div class="art" role="img" aria-label="Illustration of two arguing parents with a child between them" style="left:22px;top:742px;width:360px;height:110px;background:linear-gradient(90deg,#2e6b3c,#f0c75a 50%,#e6b84a)"></div>

    <p class="txt sky abs" style="left:28px;top:860px">5. Failing to provide your child with<br>regular medical attiontion, despite<br>your income.</p>
    <div class="art" role="img" aria-label="Illustration of a sick child being told it is nothing" style="left:20px;top:956px;width:350px;height:80px;background:linear-gradient(90deg,#3a3d20,#5a2f1f 50%,#3a3d20)"></div>

    <p class="txt lime abs" style="left:28px;top:1044px">6. Failing to give your child<br>adequate attention, regardless<br>of your time constraints, and<br>refusing help from others.</p>
    <div class="art" role="img" aria-label="Illustration of a crossed-out clock" style="left:304px;top:1090px;width:88px;height:88px;border-radius:50%;background:linear-gradient(135deg,#2c5eb0,#e23a3a)"></div>
  </section>

  <section class="col col-consequences">
    <p class="txt sky abs" style="left:30px;top:34px">7. Allowing your child to wear clothes<br>that are deemed inappropriate for the<br>weather, their age, etc.</p>
    <p class="txt lime abs" style="left:26px;top:140px">8. Not being present<br>if/when your child<br>throws a party in<br>your home.</p>
    <div class="art" role="img" aria-label="Illustration of a child in summer clothes standing in the rain" style="left:206px;top:134px;width:170px;height:136px;background:linear-gradient(180deg,#3e4443,#c64a3a 50%,#8fc6e8)"></div>

    <div class="big-num abs" style="left:22px;top:278px;font-size:104px">7</div>
    <h2 class="head abs" style="left:76px;top:276px;font-size:36px">Consequences of a</h2>
    <div class="head abs" style="left:75px;top:304px;font-size:52px">Child Neglect</div>
    <div class="head abs" style="left:75px;top:344px;font-size:52px">Charge</div>
    <div class="art" role="img" aria-label="Illustration of a child behind jail bars" style="left:270px;top:360px;width:110px;height:92px;border-radius:2px;background:linear-gradient(90deg,#7a7a7a,#f0cf6a 50%,#7a7a7a)"></div>

    <ol class="penalties abs" style="left:26px;top:404px">
      <li class="txt sun">1. Jail time</li>
      <li class="txt sun">2. The loss of custody<br>or parental rights</li>
      <li class="txt sun">3. Fines</li>
      <li class="txt sun">4. An injunction</li>
      <li class="txt sun">5. Registration as a sex offender</li>
      <li class="txt sun">6. Restrictions on probation<br>and parole</li>
      <li class="txt sun">7. Involuntary<br>commitment to<br>a mental<br>institution</li>
    </ol>
    <div class="money abs" style="left:228px;top:494px">$$$</div>
    <div class="art" role="img" aria-label="Illustration of a rolled paper document" style="left:216px;top:666px;width:156px;height:154px;border-radius:4px;background:var(--paper)"></div>

    <p class="note abs" style="left:26px;top:840px"><span class="org">National Council for Safe Childhoods (NCSC),</span><br>defines neglect as failing to meet a child's<br>physical, emotional and educational needs,<br>as well as failure to provide a child with<br>proper supervision.</p>
    <div class="art" role="img" aria-label="Illustration of a broken heart beside a confused, lonely child" style="left:60px;top:1020px;width:320px;height:146px;background:linear-gradient(90deg,#f2a28e,#0e2622 40%,#e6823a 70%,#2f5aa0)"></div>
  </section>

  <section class="col col-avoid">
    <div class="big-num abs" style="left:70px;top:36px;font-size:108px">6</div>
    <h2 class="head abs" style="left:120px;top:28px;font-size:38px">Ways to avoid</h2>
    <div class="head abs" style="left:120px;top:58px;font-size:52px">Child Neglect</div>
    <div class="head abs" style="left:120px;top:96px;font-size:52px">Charges</div>

    <p class="txt sun abs" style="left:24px;top:164px">1. Make sure that your child is well su-<br>pervised by a trusted adult if you will<br>not be home.</p>
    <div class="art" role="img" aria-label="Illustration of a smiling child with a caring adult" style="left:150px;top:258px;width:222px;height:96px;background:linear-gradient(90deg,#3a6d32,#f3c451 60%,#ffffff)"></div>

    <p class="txt sun abs" style="left:24px;top:360px">2. Ensure that your child has adequate<br>health/hygiene products.</p>
    <p class="txt sun abs" style="left:24px;top:434px">3. Ensure that your<br>child is receiving<br>regular quality<br>health care.</p>
    <div class="art" role="img" aria-label="Illustration of a sick child resting in bed" style="left:206px;top:426px;width:156px;height:126px;background:linear-gradient(180deg,#f3c2dc,#ee8db8)"></div>

    <p class="txt sun abs" style="left:24px;top:570px">4. Avoid getting into altercations with<br>your child's other parent if/when your<br>child is around.</p>
    <p class="txt sun abs" style="left:24px;top:674px">5. Keep an eye on<br>your child if/when<br>they are playing<br>outside, whether<br>they are on your<br>property, or you're<br>away from the home<br>at a playground,<br>friend's house, etc.</p>
    <div class="art" role="img" aria-label="Illustration of a happy family and a child on a parent's shoulders" style="left:206px;top:666px;width:180px;height:282px;background:linear-gradient(180deg,#2e6b3c,#f1c95c 35%,#e0472e 70%,#3a8a3e)"></div>

    <p class="txt sun abs" style="left:24px;top:964px">6. Avoid handling chores that require<br>your full attention when on-the-go with<br>your child(ren).</p>

    <svg class="abs" style="left:168px;top:1042px" width="212" height="50" viewBox="0 0 212 52" aria-hidden="true">
      <g fill="var(--sun)">
        <path d="M14 0h12v28h12L20 52 2 28h12z"/>
        <path d="M68 0h12v28h12L74 52 56 28h12z"/>
        <path d="M122 0h12v28h12l-18 24-18-24h12z"/>
        <path d="M176 0h12v28h12l-18 24-18-24h12z"/>
      </g>
    </svg>
    <div class="sources-label abs" style="left:24px;top:1072px">Sources:</div>
    <ul class="source-list abs" style="left:24px;top:1098px;width:336px">
      <li>https://www.familymindjournal.org/conditions/child-neglect</li>
      <li>http://www.riverbendhealth.edu/health/medical/ency/articles/child-neglect-and-psychological-abuse</li>
      <li>https://www.lawguidehub.org/article.asp?id=31009</li>
    </ul>
  </section>

</main>
</body>
</html>
```